Design signage for shop front glass windows

Our clinic is called Wattlebrook Medical Practice and we are a general practice offering medical services. Our services include
1. General Practice Consultations
2. Immunisations
3. Health checks
4. Women's health
5. Men's Health
6. Skin cancer checks
7. Travel medicine
8. Referrals
9. Antenatal checks
10. Minor surgery
11. Cosmetic medicine
12. Pre Employment Medicals
13. Diabetes care
14. Wound care
and much more

Our motto is
"friendly and professional health care for you and your family"

We also have a range of allied health services
including
Psychology
Physiotherapy
Podiatry
Dietetics and Nutrition
Exercise Physiology
Diabetes Education

On the signs there should be the words "Bulk Billing for GP services'
"Book online at www.wattlebrookmedicalpractice.example.au"
"Ph: 07 5196 4208"

We have glass windows on our shopfront - there are 11 panels (see attached photos) - 3 panels on the left have a white film and 4 panels in the centre are just tinted (no further signage will be installed on the central glass doors which are not included). There are another 4 panels on the right that have a white film. We are looking for a design for the glass signage to promote our services. We will print signage that can be stuck on the glass. There will need to be more bold signage on the white film and more subtle minor signage on the tinted glass windows which can still allow light thru. I have attached pictures of the window. Our logo is on our website www.wattlebrookmedicalpractice.example.au to get an idea of colours.

Target Market(s)

Young families living in the region of Capalaba Queensland

Industry/Entity Type

Health Care

Font styles to use
Serif

Colors
85abd2
acd036
ec1f27

Requirements
Must have
• The words
• "Bulk Billing for General Practice Services"
• "friendly and professional health care for you and your family"
• Book online at www.wattlebrookmedicalpractice.example.au
• Phone 07 5196 4208

```html
<!DOCTYPE html>
<html lang="en">
<head>
<meta charset="utf-8">
<title>Wattlebrook Medical Practice – Window Signage</title>
<link rel="stylesheet" href="https://fonts.googleapis.com/css2?family=Barlow:wght@500;600;700&family=Open+Sans:ital,wght@0,600;1,600&family=Roboto:wght@400;700;900&display=swap">
<style>
  :root {
    --bg: #e4e4e4;
    --white: #ffffff;
    --green: #0ba64e;
    --green-dark: #08893f;
    --lime: #c6f21c;
    --red: #e8232b;
    --ink: #111111;
  }
  * { box-sizing: border-box; margin: 0; padding: 0; }
  html, body { width: 1200px; height: 1000px; overflow: hidden; }
  body { background: var(--bg); font-family: "Barlow", Arial, sans-serif; position: relative; }

  .banner {
    position: absolute; top: 37px; width: 362px; height: 925px;
    background: var(--white);
    box-shadow: 0 14px 18px -10px rgba(0,0,0,.45);
  }
  .banner--services { left: 213px; }
  .banner--allied { left: 613px; }
  .banner__field { position: absolute; inset: 0; }

  .t { position: absolute; left: 0; right: 0; text-align: center; transform: translateY(-50%); white-space: nowrap; }

  .brand-name {
    font-family: "Open Sans", Arial, sans-serif; font-weight: 600; font-size: 22px;
    color: var(--green-dark); top: 62px;
  }
  .tagline {
    font-family: "Open Sans", Arial, sans-serif; font-style: italic; font-weight: 600;
    font-size: 14.5px; color: var(--ink); line-height: 20px; top: 116px;
  }

  .pill {
    position: absolute; left: 50%; transform: translate(-50%, -50%);
    background: var(--red); color: var(--white); border-radius: 14px;
    font-weight: 600; letter-spacing: .3px; text-align: center; white-space: nowrap;
  }
  .pill--services { top: 220px; width: 276px; height: 27px; line-height: 27px; font-size: 19px; }
  .pill--allied { top: 257px; width: 276px; height: 25px; line-height: 25px; font-size: 18px; }

  .service-list {
    position: absolute; left: 0; right: 0; top: 241px; list-style: none;
    text-align: center; color: var(--white); font-weight: 600; font-size: 17px;
    line-height: 28.2px; letter-spacing: .3px;
  }
  .service-list li::before {
    content: ""; display: inline-block; width: 6px; height: 6px;
    background: var(--lime); margin-right: 7px; vertical-align: 3px;
  }
  .service-list .more { color: var(--lime); }
  .service-list .more::before { display: none; }

  .allied-list {
    position: absolute; left: 0; right: 0; top: 283px; list-style: none;
    text-align: center; color: var(--white); font-weight: 600; font-size: 21px;
    line-height: 29.5px; letter-spacing: .4px;
  }
  .allied-list .sep { height: 29.5px; display: flex; align-items: center; justify-content: center; }
  .allied-list .sep::before { content: ""; width: 13px; height: 13px; background: var(--lime); }

  .billing { position: absolute; left: 41px; right: 41px; border-top: 2px dotted rgba(255,255,255,.7); border-bottom: 2px dotted rgba(255,255,255,.7); text-align: center; }
  .billing--services { top: 684px; height: 72px; }
  .billing--allied { top: 676px; height: 72px; }
  .billing__title { color: var(--lime); font-weight: 700; font-size: 41px; line-height: 40px; margin-top: 7px; letter-spacing: .5px; }
  .billing__sub { color: var(--white); font-weight: 600; font-size: 15px; line-height: 16px; letter-spacing: .2px; }

  .book-label { top: 825px; font-family: "Roboto", Arial, sans-serif; font-size: 13.5px; color: var(--ink); letter-spacing: .3px; }
  .book-url { top: 844px; font-family: "Roboto", Arial, sans-serif; font-weight: 700; font-size: 15.5px; color: var(--ink); }

  .phone {
    position: absolute; left: 30px; width: 302px; top: 861px; height: 42px;
    background: var(--red); border-radius: 9px; color: var(--white);
    display: flex; align-items: center; justify-content: center; gap: 6px;
    font-family: "Roboto", Arial, sans-serif; font-weight: 900; font-size: 31px; letter-spacing: .5px;
    box-shadow: 0 4px 5px rgba(0,0,0,.35);
  }
  .phone svg { width: 22px; height: 22px; }
</style>
</head>
<body>

<section class="banner banner--services">
  <svg class="banner__field" viewBox="0 0 362 925" aria-hidden="true">
    <path fill="var(--green)" d="M0 135 L160 184 Q181 192 202 184 L362 135 V825 L202 779 Q181 772 160 779 L0 825 Z"/>
  </svg>
  <div class="t brand-name">Wattlebrook Medical Practice</div>
  <p class="t tagline">Friendly and Professional Health Care<br>for you and your family</p>
  <div class="pill pill--services">OUR SERVICES INCLUDE</div>
  <ul class="service-list">
    <li>GENERAL PRACTICE CONSULTATIONS</li>
    <li>IMMUNISATIONS</li>
    <li>HEALTH CHECKS</li>
    <li>WOMEN'S HEALTH</li>
    <li>MEN'S HEALTH</li>
    <li>SKIN CANCER CHECKS</li>
    <li>TRAVEL MEDICINE</li>
    <li>REFERRALS</li>
    <li>ANTENATAL CHECKS</li>
    <li>MINOR SURGERY</li>
    <li>COSMETIC MEDICINE</li>
    <li>PRE EMPLOYMENT MEDICALS</li>
    <li>DIABETES CARE</li>
    <li>WOUND CARE</li>
    <li class="more">AND MUCH MORE</li>
  </ul>
  <div class="billing billing--services">
    <div class="billing__title">BULK BILLING</div>
    <div class="billing__sub">FOR GENERAL PRACTICE SERVICES</div>
  </div>
  <div class="t book-label">BOOK ONLINE AT</div>
  <div class="t book-url">www.wattlebrookmedicalpractice.example.au</div>
  <div class="phone">
    <svg viewBox="0 0 24 24" aria-hidden="true"><path fill="none" stroke="#fff" stroke-width="2.2" stroke-linecap="round" stroke-linejoin="round" d="M6.5 3.5 L9 8 L7.3 9.8 Q9 13.8 14.2 16.7 L16 15 L20.5 17.5 L19 20.5 Q11 21 5.8 13.5 Q3 9 3.5 5 Z M14 3.5 Q19 4.5 20.5 10 M14 7 Q16.7 7.6 17.3 10.5"/></svg>
    <span>07 5196 4208</span>
  </div>
</section>

<section class="banner banner--allied">
  <svg class="banner__field" viewBox="0 0 362 925" aria-hidden="true">
    <path fill="var(--green)" d="M0 135 L160 184 Q181 192 202 184 L362 135 V825 L202 779 Q181 772 160 779 L0 825 Z"/>
  </svg>
  <div class="t brand-name">Wattlebrook Medical Practice</div>
  <p class="t tagline">Friendly and Professional Health Care<br>for you and your family</p>
  <div class="pill pill--allied">ALLIED HEALTH SERVICES</div>
  <ul class="allied-list">
    <li>PSYCHOLOGY</li>
    <li class="sep" aria-hidden="true"></li>
    <li>PHYSIOTHERAPY</li>
    <li class="sep" aria-hidden="true"></li>
    <li>PODIATRY</li>
    <li class="sep" aria-hidden="true"></li>
    <li>DIETETICS AND NUTRITION</li>
    <li class="sep" aria-hidden="true"></li>
    <li>EXERCISE PHYSIOLOGY</li>
    <li class="sep" aria-hidden="true"></li>
    <li>DIABETES EDUCATION</li>
  </ul>
  <div class="billing billing--allied">
    <div class="billing__title">BULK BILLING</div>
    <div class="billing__sub">FOR GENERAL PRACTICE SERVICES</div>
  </div>
  <div class="t book-label">BOOK ONLINE AT</div>
  <div class="t book-url">www.wattlebrookmedicalpractice.example.au</div>
  <div class="phone">
    <svg viewBox="0 0 24 24" aria-hidden="true"><path fill="none" stroke="#fff" stroke-width="2.2" stroke-linecap="round" stroke-linejoin="round" d="M6.5 3.5 L9 8 L7.3 9.8 Q9 13.8 14.2 16.7 L16 15 L20.5 17.5 L19 20.5 Q11 21 5.8 13.5 Q3 9 3.5 5 Z M14 3.5 Q19 4.5 20.5 10 M14 7 Q16.7 7.6 17.3 10.5"/></svg>
    <span>07 5196 4208</span>
  </div>
</section>

</body>
</html>
```